Design some Business Cards for a tax counter

Hi, I am looking to have a business card designed for my work , audit, tax accounting.

What I am looking for:

* I am looking for a double-sided business card

* Front - a place for me to include my personal information and a label (In spanish):
___________________________________________________________________
Nombre: Lucía Ferrada Montes || Asesorías laborales & Contables.
Email: lucia.ferrada.montes@correoval.example
Dirección: Av. Quilamapu nº 742 oficina 2, Rengo. (DRESS)
Celular: +569 58219047

*Label (in Spanish ): - Asesorías Tributaria
- Asesorías Laborales
______________________________________________________________________
* Back - a theme or colors, i accept ideas

**I am looking for a design that shows sales growth in some way, is very professional, and eye catching.**

Please accept ideas, be creative.

you can use a logo similar to the attachment

Files: .ai .psd. .jpg .jpeg

```html
<!DOCTYPE html>
<html lang="es">
<head>
<meta charset="utf-8">
<title>Tarjetas de presentación · Ferrada Montes</title>
<link href="https://fonts.googleapis.com/css2?family=Raleway:wght@400;600;700&family=Lato:wght@400;700&display=swap" rel="stylesheet">
<style>
  :root {
    --backdrop: #1c1c1e;
    --card: #2c2c2f;
    --teal: #2ec4d6;
    --teal-deep: #23aebf;
    --white: #f4f4f4;
    --muted: #b9bcc0;
  }
  * { margin: 0; padding: 0; box-sizing: border-box; }
  html, body { width: 1200px; height: 900px; overflow: hidden; }
  body {
    background: var(--backdrop);
    font-family: "Lato", Arial, sans-serif;
    color: var(--white);
    position: relative;
  }
  .card {
    position: absolute;
    left: 220px;
    width: 760px;
    height: 405px;
    background: var(--card);
    overflow: hidden;
  }
  .card--front { top: 32px; }
  .card--back { top: 463px; }

  .brand {
    position: absolute;
    text-align: center;
    font-family: "Raleway", Arial, sans-serif;
  }
  .brand__mark {
    display: block;
    width: 46px;
    height: 46px;
    margin: 0 auto 18px;
    background: var(--teal);
  }
  .brand__name {
    font-size: 32px;
    font-weight: 600;
    color: var(--white);
    white-space: nowrap;
  }
  .brand__tagline {
    font-size: 18px;
    font-weight: 400;
    letter-spacing: 5px;
    color: var(--muted);
    margin-top: 4px;
    white-space: nowrap;
  }
  .card--front .brand { left: 0; right: 0; top: 78px; }

  .website {
    position: absolute;
    left: 0; right: 0;
    top: 262px;
    text-align: center;
    font-family: "Raleway", Arial, sans-serif;
    font-size: 19px;
    letter-spacing: 2px;
    color: var(--muted);
  }
  .website__domain { color: var(--teal); }

  .growth-band {
    position: absolute;
    left: 0;
    bottom: 0;
    width: 760px;
    height: 110px;
  }

  .band {
    position: absolute;
    left: 0; right: 0;
    background: linear-gradient(90deg, var(--teal-deep), var(--teal));
  }
  .card--back .band { bottom: 24px; height: 52px; }

  .holder { position: absolute; left: 52px; top: 46px; }
  .holder__name {
    font-family: "Raleway", Arial, sans-serif;
    font-size: 28px;
    font-weight: 700;
  }
  .holder__role {
    font-family: "Raleway", Arial, sans-serif;
    font-size: 19px;
    color: var(--muted);
    margin-top: 2px;
  }
  .holder__rule { display: block; margin-top: 6px; }

  .card--back .brand { left: 470px; width: 260px; top: 120px; }
  .card--back .brand__name { font-size: 27px; }
  .card--back .brand__tagline { font-size: 14px; letter-spacing: 3px; line-height: 1.5; }

  .contacts {
    position: absolute;
    left: 52px;
    top: 186px;
    list-style: none;
  }
  .contact {
    display: flex;
    align-items: flex-start;
    gap: 14px;
    font-size: 19px;
    line-height: 1.2;
    margin-bottom: 16px;
  }
  .contact__icon { flex: none; width: 32px; height: 32px; margin-top: -5px; }
</style>
</head>
<body>

<section class="card card--front">
  <div class="brand">
    <span class="brand__mark"></span>
    <div class="brand__name">Ferrada Montes</div>
    <div class="brand__tagline">asesorías tributaria · laborales</div>
  </div>
  <div class="website">www.<span class="website__domain">asesoriasfm</span>.example</div>
  <svg class="growth-band" viewBox="0 0 760 110" aria-hidden="true">
    <defs>
      <linearGradient id="bandFill" x1="0" x2="1" y1="0" y2="0">
        <stop offset="0" stop-color="#23aebf"/>
        <stop offset="1" stop-color="#2ec4d6"/>
      </linearGradient>
    </defs>
    <rect x="0" y="38" width="760" height="72" fill="url(#bandFill)"/>
    <rect x="610" y="28" width="26" height="10" fill="#2ec4d6"/>
    <rect x="646" y="18" width="26" height="20" fill="#2ec4d6"/>
    <rect x="682" y="8" width="26" height="30" fill="#2ec4d6"/>
    <rect x="718" y="0" width="26" height="38" fill="#2ec4d6"/>
  </svg>
</section>

<section class="card card--back">
  <div class="holder">
    <div class="holder__name">Lucía Ferrada Montes</div>
    <div class="holder__role">Asesorías laborales &amp; Contables</div>
    <svg class="holder__rule" width="170" height="6" viewBox="0 0 170 6" aria-hidden="true">
      <line x1="0" y1="3" x2="132" y2="3" stroke="var(--teal)" stroke-width="2.5"/>
      <line x1="138" y1="3" x2="170" y2="3" stroke="var(--teal)" stroke-width="2.5" stroke-dasharray="2 4"/>
    </svg>
  </div>

  <ul class="contacts">
    <li class="contact">
      <svg class="contact__icon" viewBox="0 0 32 32" aria-hidden="true">
        <polygon points="16,1 29,8.5 29,23.5 16,31 3,23.5 3,8.5" fill="var(--teal)"/>
        <path d="M11 9.5c1-.8 2-.6 2.5.3l1.3 2.3c.4.7.2 1.4-.4 1.9l-.8.6c.7 1.7 1.9 3 3.6 3.7l.6-.8c.5-.6 1.2-.8 1.9-.4l2.3 1.3c.9.5 1.1 1.5.3 2.5-1 1.2-2.3 1.6-3.8 1-4-1.5-6.7-4.2-8.2-8.2-.6-1.5-.2-2.8 1-3.8z" fill="#fff"/>
      </svg>
      <span>+569 58219047</span>
    </li>
    <li class="contact">
      <svg class="contact__icon" viewBox="0 0 32 32" aria-hidden="true">
        <polygon points="16,1 29,8.5 29,23.5 16,31 3,23.5 3,8.5" fill="var(--teal)"/>
        <circle cx="16" cy="16" r="7" fill="none" stroke="#fff" stroke-width="1.8"/>
        <ellipse cx="16" cy="16" rx="3" ry="7" fill="none" stroke="#fff" stroke-width="1.4"/>
        <line x1="9" y1="16" x2="23" y2="16" stroke="#fff" stroke-width="1.4"/>
      </svg>
      <span>lucia.ferrada.montes@correoval.example</span>
    </li>
    <li class="contact">
      <svg class="contact__icon" viewBox="0 0 32 32" aria-hidden="true">
        <polygon points="16,1 29,8.5 29,23.5 16,31 3,23.5 3,8.5" fill="var(--teal)"/>
        <path d="M16 9l8 7h-2.4v7h-3.8v-4.5h-3.6V23h-3.8v-7H8z" fill="#fff"/>
      </svg>
      <span>Av. Quilamapu nº 742 oficina 2<br>Rengo</span>
    </li>
  </ul>

  <div class="brand">
    <span class="brand__mark"></span>
    <div class="brand__name">Ferrada Montes</div>
    <div class="brand__tagline">asesorías tributaria<br>asesorías laborales</div>
  </div>

  <div class="band"></div>
</section>

</body>
</html>
```